Property Development Business Cards

I need a business card design for Tallow Creek Developments Pty Ltd. We are a property development company in Australia and our name defines the five values that we adhere to, being Profitable, Partnerships, Quality Developments, Eco Friendly and Enduring Design.

I have attached the current logo that I use, it is just five yellow circles connected to a single cricle in the middle.

Target Market(s)

Our Target audience is real estate agents, owners of properties, builders and other trades

Industry/Entity Type

Business

Requirements
Must have
• Want to have two sides to the card, one with details and one to just highlight the company

```html
<!DOCTYPE html>
<html lang="en">
<head>
<meta charset="utf-8">
<title>Tallow Creek Developments Pty Ltd – Business Cards</title>
<link rel="stylesheet" href="https://fonts.googleapis.com/css2?family=Roboto+Condensed:wght@700&display=swap">
<style>
  :root {
    --ink: #2b303b;
    --muted: #8c8f95;
    --navy: #3b4274;
    --gold: #fdcb3e;
    --gold-deep: #f4b514;
    --paper: #ffffff;
    --swirl: #eeeeef;
  }
  * { margin: 0; padding: 0; box-sizing: border-box; }
  html, body {
    width: 1200px; height: 334px; overflow: hidden;
    background: var(--paper);
    font-family: "Roboto Condensed", "Arial Narrow", sans-serif;
  }
  .sheet { position: relative; width: 1200px; height: 334px; }
  .card {
    position: absolute; top: 0; width: 584px; height: 334px;
    background: var(--paper); overflow: hidden;
  }
  .card--front { left: 0; }
  .card--back { left: 616px; }
  .swirl-texture {
    position: absolute; border-radius: 50%;
    background: radial-gradient(circle, transparent 40%, var(--swirl) 60%, transparent 72%);
    opacity: .7;
  }
  .card--front .swirl-texture { width: 420px; height: 420px; left: -170px; top: 120px; }
  .card--front .swirl-texture.swirl-texture--top { width: 520px; height: 520px; left: 230px; top: -330px; }
  .card--back .swirl-texture { width: 460px; height: 460px; left: 330px; top: -20px; }
  .stripe-navy {
    position: absolute; left: 0; right: 0; top: 298px; height: 6px; background: var(--navy);
  }
  .stripe-gold {
    position: absolute; left: 0; right: 0; top: 313px; height: 21px; background: var(--gold);
  }
  .mark {
    position: absolute; display: flex; align-items: center; gap: 8px;
    color: var(--ink); font-weight: 700; white-space: nowrap;
  }
  .mark__dot {
    border-radius: 50%;
    background: radial-gradient(circle at 40% 35%, #fff3a6, var(--gold) 55%, var(--gold-deep));
  }
  .card--front .mark { left: 49px; top: 62px; font-size: 24px; }
  .card--front .mark__dot { width: 30px; height: 30px; }
  .card--back .mark { left: 662px; top: 42px; font-size: 17px; }
  .card--back .mark { left: 46px; }
  .card--back .mark__dot { width: 22px; height: 22px; }
  .company-name {
    position: absolute; color: var(--ink); font-weight: 700; white-space: nowrap;
    letter-spacing: -0.2px;
  }
  .card--front .company-name { left: 48px; top: 144px; font-size: 37px; }
  .card--back .company-name { left: 47px; top: 100px; font-size: 22px; }
  .values {
    position: absolute; left: 48px; top: 143px; list-style: none;
  }
  .values li {
    display: flex; align-items: center; gap: 8px;
    height: 26.4px; color: var(--muted); font-size: 14.5px; font-weight: 700;
  }
  .values svg { width: 12px; height: 12px; flex: none; }
</style>
</head>
<body>
<div class="sheet">
  <section class="card card--front">
    <div class="swirl-texture" role="img" aria-label="Faint curved line pattern"></div>
    <div class="swirl-texture swirl-texture--top" role="img" aria-label="Faint curved line pattern"></div>
    <div class="mark"><span class="mark__dot"></span>Tallow Creek</div>
    <h1 class="company-name">Tallow Creek Developments Pty Ltd</h1>
    <div class="stripe-navy"></div>
    <div class="stripe-gold"></div>
  </section>

  <section class="card card--back">
    <div class="swirl-texture" role="img" aria-label="Faint curved line pattern"></div>
    <div class="mark"><span class="mark__dot"></span>Tallow Creek</div>
    <h2 class="company-name">Tallow Creek Developments Pty Ltd</h2>
    <ul class="values">
      <li><svg viewBox="0 0 12 12" aria-hidden="true"><path d="M2 1v10" stroke="#c9a032" stroke-width="1.2"/><path d="M2.5 2l8 2.5-8 3z" fill="var(--gold)"/></svg>Profitable</li>
      <li><svg viewBox="0 0 12 12" aria-hidden="true"><path d="M2 1v10" stroke="#c9a032" stroke-width="1.2"/><path d="M2.5 2l8 2.5-8 3z" fill="var(--gold)"/></svg>Partnerships</li>
      <li><svg viewBox="0 0 12 12" aria-hidden="true"><path d="M2 1v10" stroke="#c9a032" stroke-width="1.2"/><path d="M2.5 2l8 2.5-8 3z" fill="var(--gold)"/></svg>Quality Developments</li>
      <li><svg viewBox="0 0 12 12" aria-hidden="true"><path d="M2 1v10" stroke="#c9a032" stroke-width="1.2"/><path d="M2.5 2l8 2.5-8 3z" fill="var(--gold)"/></svg>Eco Friendly</li>
      <li><svg viewBox="0 0 12 12" aria-hidden="true"><path d="M2 1v10" stroke="#c9a032" stroke-width="1.2"/><path d="M2.5 2l8 2.5-8 3z" fill="var(--gold)"/></svg>Enduring Design</li>
    </ul>
    <div class="stripe-navy"></div>
    <div class="stripe-gold"></div>
  </section>
</div>
</body>
</html>
```